Property investment company needs a letterhead design!

We are a new residential and commercial property investment company. Name of the company is Morvesta Group, LLC. We have a new logo and now we need letterhead! We prefer to have a professional and upscale appearance. We don't have any fixed requirements, so be creative! Thank you for considering this project. We are so excited to see what happens!

Target Market(s)

Professional

Industry/Entity Type

Real Estate Development

```html
<!DOCTYPE html>
<html lang="en">
<head>
<meta charset="utf-8">
<title>Morvesta Group, LLC — Letterhead</title>
<link rel="stylesheet" href="https://fonts.googleapis.com/css2?family=Poppins:wght@400;700&display=swap">
<style>
  :root {
    --navy: #172640;
    --sky: #1ea0e6;
    --paper: #ffffff;
    --mist: #e8e9eb;
  }
  * { margin: 0; padding: 0; box-sizing: border-box; }
  html, body { width: 862px; height: 1200px; overflow: hidden; background: var(--paper); }
  .letterhead {
    position: relative;
    width: 862px;
    height: 1200px;
    background: var(--paper);
    font-family: "Poppins", sans-serif;
    overflow: hidden;
  }
  .brand-name {
    position: absolute;
    left: 54px;
    top: 120px;
    width: 190px;
    text-align: center;
    color: var(--navy);
    font-weight: 700;
    line-height: 1.1;
  }
  .brand-name .word { display: block; font-size: 29px; letter-spacing: 0.5px; }
  .brand-name .suffix { display: block; font-size: 14px; letter-spacing: 4px; margin-top: 4px; }
  .backdrop-name {
    position: absolute;
    left: 0;
    top: 540px;
    width: 862px;
    text-align: center;
    color: var(--mist);
    font-weight: 700;
    line-height: 1;
  }
  .backdrop-name .word { display: block; font-size: 96px; letter-spacing: 2px; }
  .backdrop-name .suffix { display: block; font-size: 44px; letter-spacing: 18px; margin-top: 26px; }
  .contact-band {
    position: absolute;
    left: 0;
    top: 1124px;
    width: 862px;
    height: 76px;
    background: var(--navy);
  }
  .contact-list {
    position: absolute;
    left: 21px;
    top: 1150px;
    display: flex;
    align-items: center;
    list-style: none;
    color: var(--paper);
    font-size: 15.5px;
    font-weight: 400;
  }
  .contact-item { display: flex; align-items: center; gap: 8px; margin-right: 19px; white-space: nowrap; }
  .contact-icon { width: 18px; height: 18px; flex: none; }
  .seal {
    position: absolute;
    left: 698px;
    top: 1064px;
    width: 166px;
    height: 166px;
    border-radius: 50%;
    background: var(--paper);
    display: flex;
    flex-direction: column;
    align-items: center;
    justify-content: center;
    color: var(--navy);
    font-weight: 700;
    line-height: 1.1;
    padding-bottom: 30px;
  }
  .seal .word { font-size: 21px; }
  .seal .suffix { font-size: 10px; letter-spacing: 3px; margin-top: 2px; }
</style>
</head>
<body>
<main class="letterhead">
  <header class="brand-name">
    <span class="word">MORVESTA</span>
    <span class="suffix">GROUP, LLC</span>
  </header>

  <div class="backdrop-name" aria-hidden="true">
    <span class="word">MORVESTA</span>
    <span class="suffix">GROUP, LLC</span>
  </div>

  <footer class="contact-band"></footer>
  <ul class="contact-list">
    <li class="contact-item">
      <svg class="contact-icon" viewBox="0 0 20 20"><circle cx="10" cy="10" r="10" fill="var(--sky)"/><path d="M6.5 5.2l1.8-.3 1 2.4-1.2.9c.6 1.3 1.5 2.2 2.8 2.8l.9-1.2 2.4 1-.3 1.8c-4.2.3-7.7-3.2-7.4-7.4z" fill="var(--navy)"/></svg>
      <span>123 555-0187</span>
    </li>
    <li class="contact-item">
      <svg class="contact-icon" viewBox="0 0 20 20"><circle cx="10" cy="10" r="10" fill="var(--sky)"/><rect x="5.5" y="6.8" width="9" height="6.4" rx="0.8" fill="var(--navy)"/><path d="M5.8 7.2L10 10.4l4.2-3.2" stroke="var(--sky)" stroke-width="1" fill="none"/></svg>
      <span>hello@morvestagroup.com</span>
    </li>
    <li class="contact-item">
      <svg class="contact-icon" viewBox="0 0 20 20"><circle cx="10" cy="10" r="10" fill="var(--sky)"/><path d="M10 4.5a3.6 3.6 0 0 0-3.6 3.6c0 2.7 3.6 7 3.6 7s3.6-4.3 3.6-7A3.6 3.6 0 0 0 10 4.5z" fill="var(--navy)"/><circle cx="10" cy="8.1" r="1.3" fill="var(--sky)"/></svg>
      <span>Ashford Lane, Riverton IL 60412</span>
    </li>
  </ul>

  <div class="seal">
    <span class="word">MORVESTA</span>
    <span class="suffix">GROUP, LLC</span>
  </div>
</main>
</body>
</html>
```